Birchmoor Ridge Tentstays

I am Moving from rest Qo and Kestl to host my own website to create direct bookings. I haves booking platform, I just need a website to embed it into. I want a catchy website to attract potential guests to book at my accommodation located near wollin national park in Alberta, Canada.

Here is my rest Qo links:
https://www.restqo.ca/rooms/5820461937204518362?viralityEntryPoint=1&s=76

https://www.restqo.ca/rooms/5834027715963820147?viralityEntryPoint=1&s=76

https://www.restqo.ca/rooms/5907364128850273519?viralityEntryPoint=1&s=76

https://www.restqo.ca/rooms/5862173094416628305?viralityEntryPoint=1&s=76

https://www.restqo.ca/rooms/6214590837720156491?viralityEntryPoint=1&s=76

```html
<!DOCTYPE html>
<html lang="en">
<head>
<meta charset="utf-8">
<title>Birchmoor Ridge Tentstays</title>
<link href="https://fonts.googleapis.com/css2?family=Tenor+Sans&family=Hind:wght@400;500;600&display=swap" rel="stylesheet">
<style>
:root{
  --brown:#3b2721;
  --footer:#3a2921;
  --ink:#2a211d;
  --muted:#5c5450;
  --paper:#ffffff;
  --soft:#f1efee;
  --line:#d9d4d1;
  --gold:#e3b341;
}
*{box-sizing:border-box;margin:0;padding:0}
html,body{width:1200px;height:4975px;overflow:hidden}
body{position:relative;background:var(--paper);font-family:"Hind",sans-serif;color:var(--ink)}
.abs{position:absolute}
.display{font-family:"Tenor Sans",sans-serif;font-weight:400}
.center{left:0;width:1200px;text-align:center}
.btn{position:absolute;display:flex;align-items:center;justify-content:center;border-radius:30px;font-size:14px;font-weight:500}
.btn-dark{background:var(--brown);color:#fff}
.btn-light{background:#fff;color:var(--ink)}
.btn-outline{border:1.5px solid var(--ink);color:var(--ink);background:#fff}
.btn-ghost{border:1.5px solid #fff;color:#fff}
.eyebrow{font-size:14px;letter-spacing:.5px;text-transform:uppercase;color:var(--ink)}
.title{font-size:39px;color:var(--ink)}
.photo{position:absolute}

/* hero */
.hero{position:absolute;left:0;top:0;width:1200px;height:675px;
  background:linear-gradient(180deg,#c9ccd0 0%,#8c929a 25%,#5b5e4c 42%,#8b6f3c 55%,#a88a55 75%,#8f7446 100%)}
.hero .shade{position:absolute;inset:0;background:rgba(0,0,0,.18)}
.brand{position:absolute;display:flex;flex-direction:column;align-items:center;gap:6px}
.brand .mark{width:56px;height:56px;border-radius:50%;border:2px solid currentColor}
.brand .name{font-family:"Hind",sans-serif;font-weight:600;font-size:15px;letter-spacing:.5px;text-transform:uppercase;text-align:center;line-height:1.1}
.contact{position:absolute;display:flex;align-items:center;gap:10px;font-size:15px}
.nav{position:absolute;top:160px;left:0;width:1200px;height:20px;font-size:14px;color:#1f1a18}
.nav span{position:absolute;transform:translateX(-50%)}
.hero h1{position:absolute;top:265px;font-size:68px;line-height:72px;color:#fff;letter-spacing:1px}
.hero .lede{position:absolute;top:426px;font-size:15px;color:#fff}
.dots{position:absolute;top:632px;left:557px;display:flex;gap:6px}
.dots i{width:16px;height:16px;border-radius:50%;border:2px solid #fff;display:block}
.dots i.on{background:#222;border-color:#222}

/* about */
.about p.body{position:absolute;top:880px;font-size:13px;line-height:22px;color:var(--muted)}

/* accommodation */
.stays{position:absolute;left:0;top:1126px;width:1200px;height:692px;background:var(--soft)}
.card{position:absolute;background:#fff;padding:22px 16px 0 16px}
.card h3{font-size:24px;line-height:30px;text-transform:uppercase;color:var(--ink)}
.card .meta{margin-top:12px;display:flex;align-items:center;gap:8px;font-size:12px;color:var(--ink)}
.card .desc{margin-top:8px;font-size:12px;line-height:19px;color:var(--muted)}
.card .btn{font-size:12px;height:33px;top:166px}
.arrow{position:absolute;width:54px;height:54px;border-radius:50%;display:flex;align-items:center;justify-content:center}

/* experiences */
.exp{position:absolute;top:2042px;width:292px;height:445px;color:#fff}
.exp h4{position:absolute;top:253px;left:22px;font-family:"Tenor Sans",sans-serif;font-weight:400;font-size:16px;text-transform:uppercase}
.exp ul{position:absolute;top:290px;left:24px;list-style:none}
.exp li{display:flex;align-items:center;gap:10px;font-size:12px;height:22.6px}

/* bands */
.band{position:absolute;left:0;width:1200px}
.band h2{position:absolute;color:#fff}

/* footer */
.footer{position:absolute;left:0;top:4575px;width:1200px;height:400px;background:var(--footer);color:#fff}
.footer .links span{position:absolute;top:272px;transform:translateX(-50%);font-size:15px}
.footer .legal{position:absolute;top:329px;font-size:11px}
</style>
</head>
<body>

<header class="hero" role="img" aria-label="Golden autumn meadow with aspen trees and forested mountains under a cloudy sky">
  <div class="shade"></div>
  <div class="contact" style="left:150px;top:46px;color:#1f1a18">
    <svg width="24" height="24" viewBox="0 0 24 24" fill="none" stroke="#1f1a18" stroke-width="2"><path d="M5 3h4l2 5-2.5 1.5a11 11 0 0 0 6 6L16 13l5 2v4a2 2 0 0 1-2 2A16 16 0 0 1 3 5a2 2 0 0 1 2-2z"/></svg>
    +1 888-888-8888
  </div>
  <div class="brand" style="left:500px;top:16px;width:200px;color:#1f1a18">
    <span class="mark"></span>
    <span class="name">Birchmoor Ridge<br>Tentstays</span>
  </div>
  <a class="btn btn-dark" style="left:933px;top:44px;width:112px;height:32px">Book Now</a>
  <nav class="nav">
    <span style="left:277px">Home</span>
    <span style="left:365px">About Us</span>
    <span style="left:492px">Accommodation</span>
    <span style="left:629px">Experiences</span>
    <span style="left:732px">Gallery</span>
    <span style="left:821px">Reviews</span>
    <span style="left:913px">Contact</span>
  </nav>
  <h1 class="display center">Stay Where<br>The Mountains Begin.</h1>
  <p class="lede center">Luxury comfort just minutes from Wollin National Park.</p>
  <a class="btn btn-dark" style="left:514px;top:473px;width:170px;height:43px;font-size:15px">Book Your Stay</a>
  <div class="dots"><i></i><i></i><i class="on"></i><i></i></div>
</header>

<section class="about">
  <p class="eyebrow abs center" style="top:770px">About Us</p>
  <h2 class="title display abs center" style="top:800px">Your Basecamp for Adventure</h2>
  <p class="body center">Escape to the Canadian Rockies and experience nature without sacrificing comfort.<br>Our thoughtfully designed accommodations offer the perfect balance of wilderness<br>and relaxation — ideal for couples, families, and adventure seekers alike.</p>
  <a class="btn btn-dark" style="left:529px;top:980px;width:141px;height:42px;font-size:15px">Read More</a>
</section>

<section class="stays">
  <p class="eyebrow abs center" style="top:54px">Custom Adventures</p>
  <h2 class="title display abs center" style="top:90px">Accommodation</h2>

  <div class="photo" style="left:151px;top:159px;width:438px;height:284px;background:linear-gradient(160deg,#e9e3da 0%,#cfc6b8 45%,#6e6a5e 80%,#4a4640 100%)" role="img" aria-label="Interior of a dome tent with bed, chairs and a large window"></div>
  <div class="card" style="left:168px;top:377px;width:404px;height:230px">
    <h3 class="display">Dome in Aspenvale<br>County, Canada</h3>
    <div class="meta"><svg width="14" height="14" viewBox="0 0 14 14"><circle cx="7" cy="7" r="7" fill="#2a211d"/><path d="M4 7.2l2 2 4-4" stroke="#fff" stroke-width="1.6" fill="none"/></svg>4 guests &nbsp;•&nbsp; 1 bedroom &nbsp;•&nbsp; 2 beds &nbsp;•&nbsp; 1 bath</div>
    <p class="desc">Lorem ipsum dolor sit amet, consectetur adipiscing elit, sed<br>do eiusmod tempor incididunt ut labore et</p>
    <a class="btn btn-dark" style="left:16px;width:125px">View Details</a>
    <a class="btn btn-outline" style="left:157px;width:123px">Book Now</a>
  </div>

  <div class="photo" style="left:610px;top:159px;width:439px;height:284px;background:linear-gradient(180deg,#8ea1b3 0%,#5f7387 45%,#3c4c5a 75%,#2b3a3a 100%)" role="img" aria-label="Dome tent under a rainbow with evergreen forest"></div>
  <div class="card" style="left:628px;top:377px;width:404px;height:230px">
    <h3 class="display">Dome in Aspenvale<br>County, Canada</h3>
    <div class="meta"><svg width="14" height="14" viewBox="0 0 14 14"><circle cx="7" cy="7" r="7" fill="#2a211d"/><path d="M4 7.2l2 2 4-4" stroke="#fff" stroke-width="1.6" fill="none"/></svg>4 guests &nbsp;•&nbsp; 2 beds &nbsp;•&nbsp; 1 bath</div>
    <p class="desc">Lorem ipsum dolor sit amet, consectetur adipiscing elit, sed<br>do eiusmod tempor incididunt ut labore et</p>
    <a class="btn btn-dark" style="left:16px;width:125px">View Details</a>
    <a class="btn btn-outline" style="left:157px;width:123px">Book Now</a>
  </div>

  <div class="arrow" style="left:76px;top:368px;background:#8a8684">
    <svg width="18" height="18" viewBox="0 0 18 18"><path d="M11 3L5 9l6 6" stroke="#fff" stroke-width="1.6" fill="none"/></svg>
  </div>
  <div class="arrow" style="left:1065px;top:368px;background:#111">
    <svg width="18" height="18" viewBox="0 0 18 18"><path d="M7 3l6 6-6 6" stroke="#fff" stroke-width="1.6" fill="none"/></svg>
  </div>
</section>

<section class="experiences">
  <p class="eyebrow abs center" style="top:1928px">Experiences</p>
  <h2 class="title display abs center" style="top:1957px">Experiences The Rockies</h2>

  <div class="exp" style="left:151px;background:linear-gradient(180deg,#2f2f31 0%,#2a2828 45%,#3b2f27 60%,#1c1a1a 100%)" role="img" aria-label="Lake at dusk with a forested shoreline">
    <h4>World-Class Hiking Trails</h4>
    <ul>
      <li><svg width="12" height="12" viewBox="0 0 12 12"><circle cx="6" cy="6" r="6" fill="#fff"/><path d="M3.3 6.2l1.8 1.7 3.6-3.6" stroke="#222" stroke-width="1.4" fill="none"/></svg>Private Chef Option</li>
      <li><svg width="12" height="12" viewBox="0 0 12 12"><circle cx="6" cy="6" r="6" fill="#fff"/><path d="M3.3 6.2l1.8 1.7 3.6-3.6" stroke="#222" stroke-width="1.4" fill="none"/></svg>Fresh Local Seafood</li>
      <li><svg width="12" height="12" viewBox="0 0 12 12"><circle cx="6" cy="6" r="6" fill="#fff"/><path d="M3.3 6.2l1.8 1.7 3.6-3.6" stroke="#222" stroke-width="1.4" fill="none"/></svg>S'mores &amp; Snacks</li>
      <li><svg width="12" height="12" viewBox="0 0 12 12"><circle cx="6" cy="6" r="6" fill="#fff"/><path d="M3.3 6.2l1.8 1.7 3.6-3.6" stroke="#222" stroke-width="1.4" fill="none"/></svg>BBQ Grilling</li>
      <li><svg width="12" height="12" viewBox="0 0 12 12"><circle cx="6" cy="6" r="6" fill="#fff"/><path d="M3.3 6.2l1.8 1.7 3.6-3.6" stroke="#222" stroke-width="1.4" fill="none"/></svg>Pre-Stocked Fridge &amp; Cooler</li>
      <li><svg width="12" height="12" viewBox="0 0 12 12"><circle cx="6" cy="6" r="6" fill="#fff"/><path d="M3.3 6.2l1.8 1.7 3.6-3.6" stroke="#222" stroke-width="1.4" fill="none"/></svg>Farm to Table</li>
    </ul>
  </div>

  <div class="exp" style="left:454px;background:linear-gradient(180deg,#4f6a3a 0%,#3e5a2c 35%,#2d3a22 60%,#141612 100%)" role="img" aria-label="Dense green forest with a wildlife clearing">
    <h4>Wildlife Viewing</h4>
    <ul>
      <li><svg width="12" height="12" viewBox="0 0 12 12"><circle cx="6" cy="6" r="6" fill="#fff"/><path d="M3.3 6.2l1.8 1.7 3.6-3.6" stroke="#222" stroke-width="1.4" fill="none"/></svg>Wildlife Viewing</li>
      <li><svg width="12" height="12" viewBox="0 0 12 12"><circle cx="6" cy="6" r="6" fill="#fff"/><path d="M3.3 6.2l1.8 1.7 3.6-3.6" stroke="#222" stroke-width="1.4" fill="none"/></svg>Homestead Adventure</li>
      <li><svg width="12" height="12" viewBox="0 0 12 12"><circle cx="6" cy="6" r="6" fill="#fff"/><path d="M3.3 6.2l1.8 1.7 3.6-3.6" stroke="#222" stroke-width="1.4" fill="none"/></svg>Campfire Building</li>
      <li><svg width="12" height="12" viewBox="0 0 12 12"><circle cx="6" cy="6" r="6" fill="#fff"/><path d="M3.3 6.2l1.8 1.7 3.6-3.6" stroke="#222" stroke-width="1.4" fill="none"/></svg>Treasure &amp; Games</li>
      <li><svg width="12" height="12" viewBox="0 0 12 12"><circle cx="6" cy="6" r="6" fill="#fff"/><path d="M3.3 6.2l1.8 1.7 3.6-3.6" stroke="#222" stroke-width="1.4" fill="none"/></svg>Arts and Crafts</li>
      <li><svg width="12" height="12" viewBox="0 0 12 12"><circle cx="6" cy="6" r="6" fill="#fff"/><path d="M3.3 6.2l1.8 1.7 3.6-3.6" stroke="#222" stroke-width="1.4" fill="none"/></svg>Find Lost Time</li>
    </ul>
  </div>

  <div class="exp" style="left:757px;background:linear-gradient(180deg,#8a97a8 0%,#5a6a80 30%,#36455a 55%,#111820 100%)" role="img" aria-label="Dome tent among bare winter trees at twilight">
    <h4>Winter Snow Adventures</h4>
    <ul>
      <li><svg width="12" height="12" viewBox="0 0 12 12"><circle cx="6" cy="6" r="6" fill="#fff"/><path d="M3.3 6.2l1.8 1.7 3.6-3.6" stroke="#222" stroke-width="1.4" fill="none"/></svg>Nature Immersion</li>
      <li><svg width="12" height="12" viewBox="0 0 12 12"><circle cx="6" cy="6" r="6" fill="#fff"/><path d="M3.3 6.2l1.8 1.7 3.6-3.6" stroke="#222" stroke-width="1.4" fill="none"/></svg>Meditation Tools</li>
      <li><svg width="12" height="12" viewBox="0 0 12 12"><circle cx="6" cy="6" r="6" fill="#fff"/><path d="M3.3 6.2l1.8 1.7 3.6-3.6" stroke="#222" stroke-width="1.4" fill="none"/></svg>Bird Watching</li>
      <li><svg width="12" height="12" viewBox="0 0 12 12"><circle cx="6" cy="6" r="6" fill="#fff"/><path d="M3.3 6.2l1.8 1.7 3.6-3.6" stroke="#222" stroke-width="1.4" fill="none"/></svg>Aroma Therapy</li>
      <li><svg width="12" height="12" viewBox="0 0 12 12"><circle cx="6" cy="6" r="6" fill="#fff"/><path d="M3.3 6.2l1.8 1.7 3.6-3.6" stroke="#222" stroke-width="1.4" fill="none"/></svg>Earthing/Grounding</li>
      <li><svg width="12" height="12" viewBox="0 0 12 12"><circle cx="6" cy="6" r="6" fill="#fff"/><path d="M3.3 6.2l1.8 1.7 3.6-3.6" stroke="#222" stroke-width="1.4" fill="none"/></svg>Top Deck Yoga</li>
    </ul>
  </div>
</section>

<section class="band" style="top:2631px;height:619px;background:linear-gradient(180deg,#4d5566 0%,#3c4354 40%,#262a30 65%,#1c1a1a 100%)" role="img" aria-label="Silhouetted forest at dusk with a lit dome tent in the foreground">
  <h2 class="display center" style="top:227px;font-size:60px">Book Directly With Us</h2>
  <a class="btn btn-light" style="left:539px;top:323px;width:122px;height:31px;font-size:15px">Book Now</a>
</section>

<section class="gallery">
  <p class="eyebrow abs center" style="top:3356px">Photos</p>
  <h2 class="title display abs center" style="top:3381px">Our Gallery</h2>
  <div class="photo" style="left:151px;top:3466px;width:291px;height:435px;background:linear-gradient(170deg,#3d2f63 0%,#6a3f8a 25%,#2f7a5c 50%,#1b2b33 75%,#111418 100%)" role="img" aria-label="Purple and green northern lights over a dark treeline"></div>
  <a class="btn btn-ghost" style="left:151px;top:3837px;width:131px;height:46px;border-radius:0 30px 30px 0;border-left:none;justify-content:flex-start;padding-left:26px;font-size:15px">WOLLIN</a>
  <div class="photo" style="left:454px;top:3466px;width:292px;height:435px;background:linear-gradient(180deg,#c7cbd0 0%,#7e8790 25%,#555b46 40%,#a48840 60%,#8a7142 100%)" role="img" aria-label="Autumn meadow with golden aspens under a cloudy sky"></div>
  <div class="photo" style="left:755px;top:3466px;width:294px;height:211px;background:linear-gradient(180deg,#1e2a44 0%,#2c4f5a 45%,#27433a 65%,#121617 100%)" role="img" aria-label="Green aurora over a campsite at night"></div>
  <div class="photo" style="left:755px;top:3692px;width:294px;height:209px;background:linear-gradient(180deg,#ece5da 0%,#d7cbb8 50%,#8a6a4a 85%,#6c4f36 100%)" role="img" aria-label="Dome interior with bed, telescope and wooden floor"></div>
</section>

<section class="band" style="top:4090px;height:485px;background:linear-gradient(180deg,#333532 0%,#2b2d2b 50%,#242423 100%)" role="img" aria-label="Dome tent and small cabin among trees in evening light">
  <h2 class="display center" style="top:122px;font-size:62px;line-height:62px">Ready for Your<br>Mountain Escape?</h2>
  <p class="center abs" style="top:282px;font-size:28px;color:#fff">Duis aute irure dolor in reprehenderit</p>
  <a class="btn btn-light" style="left:518px;top:346px;width:162px;height:29px;font-size:12px">Book Now</a>
</section>

<footer class="footer">
  <div class="contact" style="left:151px;top:122px">
    <svg width="24" height="24" viewBox="0 0 24 24" fill="none" stroke="#e3b341" stroke-width="2"><path d="M5 3h4l2 5-2.5 1.5a11 11 0 0 0 6 6L16 13l5 2v4a2 2 0 0 1-2 2A16 16 0 0 1 3 5a2 2 0 0 1 2-2z"/></svg>
    +1 888-888-8888
  </div>
  <div class="contact" style="left:151px;top:177px;font-size:14px">
    <svg width="24" height="18" viewBox="0 0 24 18"><rect x="1" y="1" width="22" height="16" rx="1" fill="#e3b341"/><path d="M1 1l11 9 11-9" stroke="#3a2921" stroke-width="1.6" fill="none"/></svg>
    info@birchmoorridgetentstays.com
  </div>
  <div class="brand" style="left:495px;top:90px;width:210px;color:#fff">
    <span class="mark"></span>
    <span class="name">Birchmoor Ridge<br>Tentstays</span>
  </div>
  <a class="btn btn-ghost" style="left:860px;top:116px;width:164px;height:33px;font-size:15px">Book Now</a>
  <div class="contact" style="left:826px;top:170px;font-size:14px;line-height:19px">
    <svg width="20" height="26" viewBox="0 0 20 26"><path d="M10 1a8 8 0 0 0-8 8c0 6 8 15 8 15s8-9 8-15a8 8 0 0 0-8-8z" fill="#e3b341"/><circle cx="10" cy="9" r="3" fill="#3a2921"/></svg>
    <span>2275 Larchfield Trail<br>in Westmere Valley.</span>
  </div>
  <nav class="links">
    <span style="left:261px">Home</span>
    <span style="left:354px">About Us</span>
    <span style="left:487px">Accommodation</span>
    <span style="left:632px">Experiences</span>
    <span style="left:740px">Gallery</span>
    <span style="left:833px">Reviews</span>
    <span style="left:929px">Contact</span>
  </nav>
  <p class="legal" style="left:157px">© 2026 All Rights Reserved | Company Name</p>
  <p class="legal" style="left:868px">Privacy Policy &nbsp;/&nbsp; Terms of Use</p>
</footer>

</body>
</html>
```